Varnel Quillbrook Comprehensive Ketamine Therapy Landing Page

We are an existing psychiatry clinic that will be offering a comprehensive ketamine therapy program and need a landing page. The landing page is well outlined with copy in the attached PDF. I've also attached what our current homepage looks like to get a sense of our brand and pictures of our practitioners for the landing page. Landing page should be sleek, modern, professional, and easy to navigate. Our brand is avant-garde mental health treatment, sleek, modern, and mildly psychedelic. The layout should be intuitive, guiding visitors through the program's features, benefits, and bonuses seamlessly. Proprietary infographics or AI-generated art is welcome. Ensure the design is responsive, with clear, compelling calls-to-action leading to a straightforward sign-up or contact process. https://files.brennowshare.net/folders/7kqTz2Lm9RwXa4VbN8pJd0sHy3cUe61Gf?usp=sharing

```html
<!DOCTYPE html>
<html lang="en">
<head>
<meta charset="utf-8">
<title>Varnel Quillbrook – Ketamine Therapy Program</title>
<link href="https://fonts.googleapis.com/css2?family=Poppins:ital,wght@0,300;0,400;0,500;0,600;1,400&display=swap" rel="stylesheet">
<style>
:root{
  --violet:#44227b; --indigo:#20357e; --navy:#13447b; --ocean:#0c597f; --teal:#078e83;
  --deep:#0f2258; --ink:#1b1f33; --muted:#6b7085; --line:#e3e5ee; --bg:#d0d6df;
}
*{box-sizing:border-box;margin:0;padding:0}
html,body{width:1200px;height:4520px;overflow:hidden;background:var(--bg);font-family:"Poppins",sans-serif;color:var(--ink)}
.page{position:absolute;left:212px;top:300px;width:782px;height:4106px;background:#fff;overflow:hidden}
.glow{position:absolute;border-radius:50%;filter:blur(60px);opacity:.35}
.abs{position:absolute}
.brand{display:flex;align-items:center;gap:7px;font-weight:600;font-size:12px;letter-spacing:.5px}
.brand i{width:14px;height:14px;border-radius:50%;background:currentColor;display:block}
.hero{left:9px;top:5px;width:763px;height:391px;border-radius:22px;overflow:hidden;background:linear-gradient(100deg,#141a4a 0%,#1e2466 45%,#3a2a78 100%)}
.hero-art{position:absolute;right:0;top:0;width:430px;height:100%;background:radial-gradient(circle at 60% 35%,#a35bd6 0%,#5a3aa8 30%,#2a2a70 60%,transparent 80%),radial-gradient(circle at 75% 80%,#2c6fbf 0%,transparent 50%)}
.hero .brand{position:absolute;left:62px;top:16px;color:#fff}
.hero h1{position:absolute;left:49px;top:92px;width:350px;color:#fff;font-weight:500;font-size:30px;line-height:33px}
.hero p{position:absolute;left:50px;top:240px;width:320px;color:#e6e8ff;font-size:11px;line-height:16px}
.pill{display:inline-flex;align-items:center;gap:10px;height:26px;padding:0 16px;border-radius:14px;font-size:8.5px;font-weight:500}
.pill.white{background:#fff;color:var(--indigo)}
.pill.dark{background:var(--indigo);color:#fff}
.pill.ghost{border:1px solid var(--indigo);color:var(--indigo);background:#fff}
.hero .pill{position:absolute;left:50px;top:290px;padding:0 18px}
.ph{position:absolute;border-radius:14px}
h2{font-weight:500;font-size:27px;line-height:31px}
h2 em{font-style:normal;background:linear-gradient(90deg,var(--violet),var(--teal));-webkit-background-clip:text;background-clip:text;color:transparent}
.center{left:0;width:782px;text-align:center}
.copy{font-size:8.5px;line-height:13.5px;color:var(--muted)}
.copy b{color:var(--ink)}
.wave-label{position:absolute;font-size:8.5px;color:var(--muted);text-align:center;width:110px}
.small{font-size:8px;color:var(--muted)}
.cta{display:flex;justify-content:center;gap:8px}
.tabs{left:58px;top:1349px;width:665px;display:flex;justify-content:space-between;border-bottom:1px solid var(--line);padding-bottom:14px}
.tabs span{font-size:7px;line-height:9px;color:var(--muted);text-align:center;width:56px}
.tabs span.on{color:var(--indigo)}
h3{font-weight:500;font-size:16px}
.member{position:absolute;width:146px;text-align:center}
.member .ph{position:relative;width:146px;height:189px;border-radius:10px;display:block}
.member b{display:block;font-weight:400;font-size:9.5px;margin-top:18px}
.member small{font-size:6.5px;color:var(--muted)}
.bonus{left:9px;top:2149px;width:763px;height:319px;border-radius:22px;background:var(--deep)}
.bonus-list{left:421px;top:2278px;width:310px}
.bonus-list div{display:flex;justify-content:space-between;align-items:center;height:37px;border-bottom:1px solid rgba(255,255,255,.18);color:#fff;font-size:9px;padding:0 4px}
.testi{left:14px;top:2791px;width:753px;height:408px;border-radius:22px;background:var(--deep);color:#fff;text-align:center}
.faq{position:absolute;width:326px;height:32px;border:1px solid var(--line);border-radius:10px;display:flex;align-items:center;justify-content:space-between;padding:0 12px;font-size:7.5px;color:var(--muted)}
.faq i{width:12px;height:12px;border:1px solid var(--muted);border-radius:50%;font-style:normal;font-size:10px;line-height:10px;text-align:center}
.field{position:absolute;left:58px;width:262px;border-bottom:1px solid var(--line);padding-bottom:6px}
.field b{display:block;font-weight:400;font-size:8px}
.field span{font-size:6.5px;color:#a0a4b5}
.footer{left:58px;top:4068px;width:665px;display:flex;justify-content:space-between;align-items:center;font-size:6.5px;color:var(--muted)}
</style>
</head>
<body>
<main class="page">
  <div class="glow" style="left:-80px;top:1000px;width:300px;height:300px;background:#c8a6ff"></div>
  <div class="glow" style="right:-80px;top:1080px;width:280px;height:280px;background:#8fe9e1"></div>
  <div class="glow" style="left:300px;top:1880px;width:320px;height:260px;background:#e0c0ff"></div>
  <div class="glow" style="left:-60px;top:2850px;width:300px;height:260px;background:#d5b8ff"></div>
  <div class="glow" style="right:-60px;top:3500px;width:260px;height:260px;background:#a9efe8"></div>
  <div class="glow" style="left:-40px;top:3900px;width:260px;height:220px;background:#d5c0ff"></div>

  <section class="abs hero">
    <div class="hero-art" role="img" aria-label="Profile of a woman with a glowing neural network above her head"></div>
    <div class="brand"><i></i>Varnel Psychiatry</div>
    <h1>Begin your Odyssey: Transform Your Life Across 6 Dimensions of Wellness</h1>
    <p>The World's Most Comprehensive Ketamine Program, Right here in Colorado!</p>
    <span class="pill white">Explore the Benefits <span>›</span></span>
  </section>

  <section>
    <div class="ph" style="left:58px;top:512px;width:323px;height:333px;background:radial-gradient(circle at 50% 40%,#8ec5ff 0%,#2f6fd0 40%,#0c2a78 80%)" role="img" aria-label="Illustration of a glowing brain on a pedestal"></div>
    <div class="abs" style="left:421px;top:524px;width:320px">
      <h2 style="font-size:26px;line-height:31px">Discover the<br><em>Transformative Power</em><br>of Ketamine Therapy</h2>
      <p class="copy" style="margin-top:22px">Our psychiatrists conduct the medical evaluation to gain a comprehensive understanding of your health. This process ensures potential risks, contraindications, and individualized considerations are carefully evaluated. It allows for a safer and more personalized therapeutic experience.</p>
      <p class="copy" style="margin-top:9px">But that's not all. This program goes <b>much</b> further than just ketamine therapy...</p>
      <p class="copy" style="margin-top:9px">We take you on a completely comprehensive 90-day journey designed to make lasting change in EVERY area of your life. During this experience you will be accompanied by some of the world's best mental health practitioners. It offers not just symptom relief, but a path towards deep, enduring healing and personal transformation.</p>
    </div>
  </section>

  <section>
    <h2 class="abs center" style="top:915px">The <em>Benefits</em> of the<br>Varnel Program</h2>
    <svg class="abs" style="left:114px;top:1000px" width="569" height="140" viewBox="0 0 569 140">
      <defs><linearGradient id="wg" x1="0" x2="1"><stop offset="0" stop-color="#44227b"/><stop offset=".5" stop-color="#20357e"/><stop offset="1" stop-color="#0c597f"/></linearGradient>
      <filter id="sh"><feDropShadow dx="0" dy="3" stdDeviation="4" flood-color="#20357e" flood-opacity=".15"/></filter></defs>
      <path d="M4 68 A56 56 0 0 1 116 68 A56 56 0 0 0 228 68 A56 56 0 0 1 340 68 A56 56 0 0 0 452 68 A56 56 0 0 1 564 68" fill="none" stroke="url(#wg)" stroke-width="5" stroke-linecap="round"/>
      <g filter="url(#sh)" fill="#fff"><circle cx="60" cy="68" r="42"/><circle cx="172" cy="68" r="42"/><circle cx="284" cy="68" r="42"/><circle cx="396" cy="68" r="42"/><circle cx="508" cy="68" r="42"/></g>
      <g fill="none" stroke="#20357e" stroke-width="1.5">
        <circle cx="60" cy="68" r="13"/><path d="M60 60v8l6 4"/>
        <path d="M160 58h6M160 66h6M160 74h6M170 58h14M170 66h14M170 74h14"/>
        <circle cx="284" cy="68" r="13"/><circle cx="284" cy="68" r="6"/><path d="M284 55v-3M297 68h3"/>
        <circle cx="396" cy="63" r="9"/><path d="M390 70l-4 12 6-3 4 5 4-5 6 3-4-12"/>
        <circle cx="508" cy="68" r="12"/><path d="M508 52v4M508 80v4M492 68h4M520 68h4M497 57l3 3M516 76l3 3M519 57l-3 3M500 76l-3 3"/>
      </g>
    </svg>
    <div class="wave-label" style="left:119px;top:1118px">Quick and<br>Effective</div>
    <div class="wave-label" style="left:231px;top:996px">Comprehensive</div>
    <div class="wave-label" style="left:343px;top:1118px">Personalized<br>to You</div>
    <div class="wave-label" style="left:455px;top:996px">Exclusive</div>
    <div class="wave-label" style="left:567px;top:1118px">Complete<br>Transformation</div>
    <p class="abs center small" style="top:1170px;font-size:7px">Sign up (We are now accepting 3 people for the initial cohort)</p>
    <div class="abs center cta" style="top:1188px"><span class="pill dark">Set Up Free Consultation ›</span><span class="pill ghost">Join the Waitlist Today ›</span></div>
  </section>

  <section>
    <h2 class="abs center" style="top:1298px">Program <em>Offerings</em></h2>
    <div class="abs tabs">
      <span class="on">1 Medical Evaluation</span><span>1 Preparation Session</span><span>6 Ketamine Assisted Therapy Sessions</span><span>6 Integration Sessions</span><span>Nutrition &amp; Movement Coaching</span><span>Labs and Micronutrient Testing</span><span>Mindfulness Coaching</span><span>Spiritual Coaching</span><span>Hypnotherapy or EMDR</span><span>Holotropic Breathwork</span>
    </div>
    <div class="abs" style="left:58px;top:1388px;width:40px;height:3px;background:var(--indigo)"></div>
    <div class="abs" style="left:100px;top:1490px;width:270px">
      <h3>1 Medical Evaluation</h3>
      <p class="copy" style="margin-top:14px">Our psychiatrists conduct the medical evaluation to gain a comprehensive understanding of your health. This process ensures potential risks, contraindications, and individualized considerations are carefully evaluated. It allows for a safer and more personalized therapeutic experience.</p>
    </div>
    <div class="ph" style="left:411px;top:1431px;width:312px;height:223px;background:linear-gradient(135deg,#8a6c58,#c9b3a0 50%,#6d7fa8)" role="img" aria-label="Photo of a patient talking with a psychiatrist"></div>
  </section>

  <section>
    <h2 class="abs center" style="top:1738px">Our Team</h2>
    <p class="abs small" style="left:58px;top:1775px;width:307px;text-align:center;font-size:7px">Practitioners</p>
    <p class="abs small" style="left:414px;top:1778px;width:308px;text-align:center;font-size:7px">Trainers</p>
    <div class="member" style="left:58px;top:1798px"><span class="ph" style="background:linear-gradient(#e9e3f4,#c9c4d8)" role="img" aria-label="Portrait of a practitioner"></span><b>Dr. Rufus Penn</b><small>Expand Info +</small></div>
    <div class="member" style="left:219px;top:1798px"><span class="ph" style="background:linear-gradient(#eceef2,#c8ccd4)" role="img" aria-label="Portrait of a practitioner"></span><b>Owen Tallis LPC</b><small>Expand Info +</small></div>
    <div class="member" style="left:414px;top:1798px"><span class="ph" style="background:linear-gradient(#eceef2,#cbc6c2)" role="img" aria-label="Portrait of a trainer"></span><b>Milo Harcourt</b><small>Expand Info +</small></div>
    <div class="member" style="left:576px;top:1798px"><span class="ph" style="background:linear-gradient(#eaf0f6,#c2cad8)" role="img" aria-label="Portrait of a trainer"></span><b>Dr. Victor Lam</b><small>Expand Info +</small></div>
    <div class="abs" style="left:390px;top:1798px;width:1px;height:273px;background:var(--line)"></div>
    <div class="abs small" style="left:188px;top:2041px;font-size:12px;letter-spacing:8px"><span style="color:#bbb">←</span><span style="color:var(--indigo)">→</span></div>
    <div class="abs small" style="left:553px;top:2041px;font-size:12px;letter-spacing:8px"><span style="color:#bbb">←</span><span style="color:var(--indigo)">→</span></div>
    <div class="abs" style="left:58px;top:2071px;width:665px;height:1px;background:var(--line)"></div>
  </section>

  <section>
    <div class="abs bonus"></div>
    <div class="ph" style="left:58px;top:2226px;width:323px;height:319px;border-radius:6px;background:linear-gradient(160deg,#9a6a5c,#4e7d95 45%,#c8d3de 70%,#5a6f86)" role="img" aria-label="Double exposure of a woman's profile with a lake landscape"></div>
    <h2 class="abs" style="left:421px;top:2233px;color:#fff;font-size:25px">Bonuses (Added Free)</h2>
    <div class="abs bonus-list">
      <div><span>01 - Masterclass Workshops</span><span>⌄</span></div>
      <div><span>02 - Weekly Quests</span><span>⌄</span></div>
      <div><span>03 - Free massage gun in the mail upon signing up!</span><span>⌄</span></div>
      <div><span>04 - Yoga Classes or Gym Membership</span><span>⌄</span></div>
    </div>
  </section>

  <section>
    <h2 class="abs center" style="top:2627px">Our <em>Guarantee</em> to<br>Our Clients</h2>
    <p class="abs center small" style="top:2697px;line-height:13px">Today, there is no other program like this in the world!<br>Pay nothing until after your medical &amp; psychiatric evaluation</p>
  </section>

  <section class="abs testi">
    <h2 style="margin-top:72px">Testimonials</h2>
    <p style="font-size:8px;opacity:.75;margin-top:10px">See what people have said about our ketamine programs</p>
    <svg width="30" height="22" viewBox="0 0 30 22" style="margin-top:18px"><path d="M0 0h12v12l-5 10H2l4-10H0zM17 0h12v12l-5 10h-5l4-10h-6z" fill="#9fb0d8"/></svg>
    <p style="font-style:italic;font-size:10px;line-height:16px;width:420px;margin:8px auto 0">"Dr. Penn is an exceptionally talented and capable psychiatrist. The depth and breadth of his knowledge are outstanding. He served with distinction as Chief Resident and is a strong advocate for his patients."</p>
    <div role="img" aria-label="Portrait of the reviewer" style="width:44px;height:44px;border-radius:50%;background:linear-gradient(#e8d8cc,#b89a86);border:2px solid #fff;margin:22px auto 0"></div>
    <p style="font-size:8.5px;font-weight:500;margin-top:8px">Dr. Helena Marchetti</p>
    <p style="font-size:6.5px;opacity:.7;line-height:9px">MD Former President of Front Range<br>Psychiatric Guild</p>
  </section>

  <section>
    <h2 class="abs center" style="top:3281px">Frequently <em>Asked</em> Questions</h2>
    <div class="faq" style="left:58px;top:3340px"><span>What is Ketamine Therapy, and how does it aid in mental health?</span><i>+</i></div>
    <div class="faq" style="left:58px;top:3387px"><span>What are the side effects of Ketamine?</span><i>+</i></div>
    <div class="faq" style="left:58px;top:3434px"><span>Can this program be done remotely?</span><i>+</i></div>
    <div class="faq" style="left:58px;top:3481px"><span>How are the Ketamine Assisted Therapy Sessions conducted?</span><i>+</i></div>
    <div class="faq" style="left:397px;top:3340px"><span>What does Ketamine feel like?</span><i>+</i></div>
    <div class="faq" style="left:397px;top:3387px"><span>Who is not right for Ketamine?</span><i>+</i></div>
    <div class="faq" style="left:397px;top:3434px"><span>What makes Varnel Quillbrook different from other therapy programs?</span><i>+</i></div>
    <div class="faq" style="left:397px;top:3481px"><span>What should I do the day of Ketamine Therapy?</span><i>+</i></div>
    <p class="abs center small" style="top:3527px;font-size:7px">Sign up (We are now accepting 3 people for the initial cohort)</p>
    <div class="abs center cta" style="top:3546px"><span class="pill dark">Set Up Free Consultation ›</span><span class="pill ghost">Join the Waitlist Today ›</span></div>
  </section>

  <section>
    <h2 class="abs" style="left:58px;top:3700px">Contact Us</h2>
    <div class="field" style="top:3743px"><b>Your Name*</b><span>Enter Your Name Here...</span></div>
    <div class="field" style="top:3787px"><b>Email Address*</b><span>Enter Your Email Here...</span></div>
    <div class="field" style="top:3831px"><b>Phone Number*</b><span>Enter Your Phone Number Here...</span></div>
    <div class="field" style="top:3875px"><b>How Can We Help?</b><span>Enter Your Enquiry Here...</span></div>
    <span class="pill dark abs" style="left:58px;top:3931px;padding:0 18px">Submit Your Request ›</span>
    <div class="ph" style="left:418px;top:3743px;width:305px;height:267px;background:linear-gradient(150deg,#6f8aa6,#3c5672 50%,#b9a690)" role="img" aria-label="Photo of a smiling man looking at his phone"></div>
  </section>

  <footer class="abs footer">
    <span>Privacy and Compliance Statement</span>
    <span class="brand" style="color:var(--indigo);font-size:11px"><i></i>Varnel Psychiatry</span>
    <span>© 2024 Varnel Psychiatry. All rights reserved</span>
  </footer>
</main>
</body>
</html>
```